Social Media Banner with Company Logo

We need company banner for social media sites: Linkedin, Twitter, and Facebook. We are looking for quality (royalty free) images of locations our customers can identify with and our company logo incorporated into those locations in a very natural way. Our customers are business owners and financial advisors. We will eventually want 12 different design concepts that all play off of the same theme of locations and our logo.

```html
<!DOCTYPE html>
<html lang="en">
<head>
<meta charset="utf-8">
<title>Steady Harbor Planning – Social Banners</title>
<link href="https://fonts.googleapis.com/css2?family=Raleway:wght@400;700&display=swap" rel="stylesheet">
<style>
  :root {
    --stage: #e2e2e2;
    --card: #ffffff;
    --brand-blue: #1a78ad;
    --deep-blue: #1b4f78;
    --brand-green: #8cc152;
    --ink: #2b2b2b;
    --tile-top: #fafafa;
    --tile-bottom: #d9d9d9;
  }
  * { margin: 0; padding: 0; box-sizing: border-box; }
  html, body { width: 1200px; height: 1200px; overflow: hidden; }
  body {
    background: radial-gradient(circle at 50% 45%, #f0f0f0 0%, var(--stage) 70%);
    font-family: "Raleway", sans-serif;
    position: relative;
  }
  .banner {
    position: absolute;
    background: var(--card);
    box-shadow: 0 6px 18px rgba(0,0,0,0.12);
    overflow: hidden;
  }
  .banner--desk { left: 260px; top: 98px; width: 681px; height: 316px; }
  .banner--meeting { left: 257px; top: 455px; width: 687px; height: 323px; }
  .banner--ideas { left: 257px; top: 818px; width: 689px; height: 277px; }

  .hero-band { position: absolute; left: 0; top: 0; width: 100%; display: block; }

  .tagline {
    position: absolute;
    border-left: 3px solid var(--brand-blue);
    padding-left: 6px;
    color: var(--ink);
    font-weight: 400;
    text-transform: uppercase;
    line-height: 0.92;
    letter-spacing: 0.2px;
  }
  .banner--desk .tagline { left: 44px; top: 54px; font-size: 26px; }
  .banner--meeting .tagline { left: 65px; top: 37px; font-size: 20px; }
  .banner--ideas .tagline { left: 70px; top: 51px; font-size: 20px; }

  .brand-tile {
    position: absolute;
    display: flex;
    align-items: center;
    justify-content: center;
    background: linear-gradient(160deg, var(--tile-top), var(--tile-bottom));
    border: 1px solid #bdbdbd;
  }
  .brand-name {
    color: var(--brand-blue);
    font-weight: 700;
    letter-spacing: 1px;
  }
  .banner--desk .brand-tile { left: 43px; top: 152px; width: 128px; height: 128px; }
  .banner--desk .brand-name { font-size: 40px; }
  .banner--meeting .brand-tile { left: 64px; top: 123px; width: 184px; height: 184px; border-radius: 22px; }
  .banner--meeting .brand-name { font-size: 58px; }
  .banner--ideas .brand-tile {
    left: 69px; top: 126px; width: 132px; height: 132px; border-radius: 50%;
    border: 5px solid #ffffff; box-shadow: 0 0 0 1px #d0d0d0;
  }
  .banner--ideas .brand-name { font-size: 40px; }
</style>
</head>
<body>

<section class="banner banner--desk">
  <svg class="hero-band" width="681" height="252" viewBox="0 0 681 252">
    <defs>
      <linearGradient id="deskFade" x1="0" y1="0" x2="1" y2="0.3">
        <stop offset="0" stop-color="#fafafa"/>
        <stop offset="0.45" stop-color="#eeeeec"/>
        <stop offset="1" stop-color="#e4e2de"/>
      </linearGradient>
      <linearGradient id="deskPhoto" x1="0" y1="1" x2="1" y2="0">
        <stop offset="0" stop-color="#3b3a3a"/>
        <stop offset="0.14" stop-color="#d9d6d0"/>
        <stop offset="0.3" stop-color="#f3f2ee"/>
        <stop offset="0.46" stop-color="#cfa98a"/>
        <stop offset="0.6" stop-color="#6d7480"/>
        <stop offset="0.74" stop-color="#4a5563"/>
        <stop offset="0.86" stop-color="#c79a62"/>
        <stop offset="1" stop-color="#f4e6cc"/>
      </linearGradient>
    </defs>
    <rect width="681" height="252" fill="url(#deskFade)"/>
    <path d="M432,0 L681,0 L681,252 L272,252 Q330,90 432,0 Z" fill="url(#deskPhoto)" role="img" aria-label="Photo: hands writing with a pen over financial charts, calculator and glasses on an office desk"/>
    <path d="M258,252 Q312,88 432,0 Q330,96 276,252 Z" fill="var(--deep-blue)"/>
    <path d="M268,252 Q320,92 432,0" fill="none" stroke="#ffffff" stroke-width="1" stroke-dasharray="3 3" opacity="0.7"/>
    <path d="M268,252 L292,232 L294,252 Z" fill="var(--brand-green)"/>
  </svg>
  <p class="tagline">Steady<br>Harbor<br>Planning</p>
  <div class="brand-tile"><span class="brand-name">SHP</span></div>
</section>

<section class="banner banner--meeting">
  <svg class="hero-band" width="687" height="229" viewBox="0 0 687 229">
    <defs>
      <linearGradient id="meetFade" x1="0" x2="1">
        <stop offset="0" stop-color="#fbf3e2"/>
        <stop offset="0.5" stop-color="#f7f3ec"/>
        <stop offset="1" stop-color="#eef0f1"/>
      </linearGradient>
      <linearGradient id="meetPhoto" x1="0" y1="0" x2="1" y2="1">
        <stop offset="0" stop-color="#d9a86b"/>
        <stop offset="0.18" stop-color="#f4eff0"/>
        <stop offset="0.32" stop-color="#c94f7a"/>
        <stop offset="0.44" stop-color="#e7c09a"/>
        <stop offset="0.56" stop-color="#3e6fa3"/>
        <stop offset="0.68" stop-color="#d9a36b"/>
        <stop offset="0.82" stop-color="#f2f0ee"/>
        <stop offset="1" stop-color="#8f8f92"/>
      </linearGradient>
    </defs>
    <rect width="687" height="229" fill="url(#meetFade)"/>
    <path d="M451,0 L687,0 L687,229 L308,229 Q362,80 451,0 Z" fill="url(#meetPhoto)" role="img" aria-label="Photo: handshake over a wooden meeting table with printed bar and pie charts and a laptop"/>
    <path d="M294,229 Q346,76 451,0 Q358,90 310,229 Z" fill="var(--deep-blue)"/>
    <path d="M304,229 L326,212 L328,229 Z" fill="var(--brand-green)"/>
  </svg>
  <p class="tagline">Steady<br>Harbor<br>Planning</p>
  <div class="brand-tile"><span class="brand-name">SHP</span></div>
</section>

<section class="banner banner--ideas">
  <svg class="hero-band" width="689" height="172" viewBox="0 0 689 172">
    <defs>
      <linearGradient id="ideasFade" x1="0" x2="1">
        <stop offset="0" stop-color="#eef1f4"/>
        <stop offset="0.6" stop-color="#e3e8ec"/>
        <stop offset="1" stop-color="#cfd5da"/>
      </linearGradient>
      <linearGradient id="ideasPhoto" x1="0" y1="1" x2="1" y2="0">
        <stop offset="0" stop-color="#2f3338"/>
        <stop offset="0.16" stop-color="#e9c8b6"/>
        <stop offset="0.3" stop-color="#6c6660"/>
        <stop offset="0.45" stop-color="#b89a80"/>
        <stop offset="0.6" stop-color="#d9d6d1"/>
        <stop offset="0.78" stop-color="#a9a7a5"/>
        <stop offset="1" stop-color="#e2e4e6"/>
      </linearGradient>
    </defs>
    <rect width="689" height="172" fill="url(#ideasFade)"/>
    <path d="M383,0 L689,0 L689,172 L274,172 Q312,60 383,0 Z" fill="url(#ideasPhoto)" role="img" aria-label="Photo: a hand touching a screen of sketched business diagrams over a city skyline at dusk"/>
    <path d="M263,172 Q300,56 383,0 Q314,66 278,172 Z" fill="var(--deep-blue)"/>
    <path d="M266,172 L290,160 L292,172 Z" fill="var(--brand-green)"/>
  </svg>
  <p class="tagline">Steady<br>Harbor<br>Planning</p>
  <div class="brand-tile"><span class="brand-name">SHP</span></div>
</section>

</body>
</html>
```